Korvell Plant Services

We are a heavy diesel mechanical business with additional air con certificates, remapping engine rebuilt

Contact Information for Business Card

Company Name, Director Name, Managing Director, Contact details, email and website

Font styles to use
Serif
Script

```html
<!DOCTYPE html>
<html lang="en">
<head>
<meta charset="utf-8">
<title>Korvell Plant Services – Business Card</title>
<link rel="stylesheet" href="https://fonts.googleapis.com/css2?family=Arimo:wght@400;700&display=swap">
<style>
  :root {
    --backdrop: #5d5f61;
    --navy: #2d2a79;
    --paper: #ffffff;
    --ink: #1c1c1f;
    --rule: #2d2a79;
  }
  * { box-sizing: border-box; margin: 0; padding: 0; }
  html, body {
    width: 1200px; height: 780px; overflow: hidden;
    background: var(--backdrop);
    font-family: "Arimo", Arial, sans-serif;
  }
  .stage {
    position: relative; width: 1200px; height: 780px;
    display: flex; align-items: center; justify-content: center; gap: 40px;
  }
  .card {
    width: 520px; height: 300px; border-radius: 26px;
    position: relative; overflow: hidden;
  }
  .card--front {
    background: var(--navy);
    display: flex; align-items: center; justify-content: center;
  }
  .brand {
    display: flex; align-items: center; gap: 12px;
    font-weight: 700; font-size: 30px; letter-spacing: 0.2px;
  }
  .brand__dot {
    width: 18px; height: 18px; border-radius: 50%;
  }
  .card--front .brand { color: var(--paper); }
  .card--front .brand__dot { background: var(--paper); }

  .card--back {
    background: var(--paper);
    display: flex; align-items: center;
    padding: 0 28px 0 26px;
  }
  .card--back .brand {
    color: var(--navy); font-size: 21px; width: 208px;
    flex-direction: column; align-items: flex-start; gap: 8px; line-height: 1.1;
  }
  .card--back .brand__dot { background: var(--navy); width: 14px; height: 14px; }
  .divider {
    width: 1.5px; height: 180px; background: var(--rule); margin: 0 22px 0 14px;
  }
  .details { color: var(--ink); font-size: 14px; line-height: 1.3; }
  .details__name {
    color: var(--navy); font-weight: 700; font-size: 21px; letter-spacing: 0.3px;
  }
  .details__title { font-size: 12px; margin-bottom: 24px; }
  .details__address { margin-bottom: 18px; }
  .contact { list-style: none; }
  .contact li { display: flex; align-items: center; gap: 8px; }
  .contact svg { width: 13px; height: 13px; fill: var(--navy); flex: none; }
</style>
</head>
<body>
<main class="stage">
  <section class="card card--front" aria-label="Card front">
    <div class="brand"><span class="brand__dot"></span>Korvell Plant Services</div>
  </section>

  <section class="card card--back" aria-label="Card back">
    <div class="brand"><span class="brand__dot"></span>Korvell<br>Plant Services</div>
    <div class="divider"></div>
    <div class="details">
      <p class="details__name">DANE WHITLOCK</p>
      <p class="details__title">Managing Director</p>
      <p class="details__address">48 C Marlow St<br>Fairhaven, TN 37990</p>
      <ul class="contact">
        <li>
          <svg viewBox="0 0 16 16"><path d="M3.5 1.5l2.5 0 1.2 3.3-1.6 1.2a8 8 0 0 0 4.4 4.4l1.2-1.6 3.3 1.2v2.5c0 .8-.7 1.5-1.5 1.5A12 12 0 0 1 2 3c0-.8.7-1.5 1.5-1.5z"/></svg>
          (615) 555-0147
        </li>
        <li>
          <svg viewBox="0 0 16 16"><path d="M1 3h14v10H1z M1.5 3.5L8 9l6.5-5.5" fill="none" stroke="#2d2a79" stroke-width="1.6"/></svg>
          hello@korvellplant.com
        </li>
        <li>
          <svg viewBox="0 0 16 16"><circle cx="8" cy="8" r="7" fill="none" stroke="#2d2a79" stroke-width="1.5"/><path d="M1 8h14M8 1c-3 3.5-3 10.5 0 14M8 1c3 3.5 3 10.5 0 14" fill="none" stroke="#2d2a79" stroke-width="1.2"/></svg>
          www.korvellplant.com
        </li>
      </ul>
    </div>
  </section>
</main>
</body>
</html>
```